Morden, Creative, Unique, Independent Wine Shop

1. We are a brand new wine shop located in Melbourne Australia, we have our logo already, simply use the logo to design a business card.
2. I have uploaded our logo in two versions, with or without shadow, any of them is acceptable.
3. Make it as creative and unique as possible, no limitation of shape, color combination, geometry pattern, fonts, composing etc.
3. Info on the card:
- Brambleford Wine Cellar (Not very necessary if logo is obviously shown)
- 42 Ferncastle Steet, Larkwood, Eastmere, Australia 3917
- +61 3 9018 4637
- www.bramblefordwinecellar.com.au
- bramblefordwinecellar@mailvista.com
- Additional icons: Google, Instagram, Facebook, Twitter
4. Once again, forget it is a commercial card, make it special.

```html
<!DOCTYPE html>
<html lang="en">
<head>
<meta charset="utf-8">
<title>Brambleford Wine Cellar – Business Card</title>
<link rel="stylesheet" href="https://fonts.googleapis.com/css2?family=Source+Sans+3:wght@400;600&display=swap">
<style>
  :root {
    --page-bg: #cfc6bb;
    --card-top: #eeebe7;
    --card-bottom: #dcd6d0;
    --card-edge: #b9b2ab;
    --wine: #7c1a2e;
    --ink: #3a3536;
    --watermark: rgba(170, 185, 200, 0.28);
  }
  * { margin: 0; padding: 0; box-sizing: border-box; }
  html, body {
    width: 1200px; height: 976px; overflow: hidden;
    background: var(--page-bg);
    font-family: "Source Sans 3", "Myriad Pro", sans-serif;
  }
  .card {
    position: absolute; left: 150px; top: 158px;
    width: 910px; height: 505px;
    border-radius: 20px;
    border: 1px solid var(--card-edge);
    background: linear-gradient(180deg, var(--card-top), var(--card-bottom));
    overflow: hidden;
  }
  .card__watermark {
    position: absolute; left: 672px; top: 12px;
    width: 234px; height: 470px; border-radius: 110px;
    background: var(--watermark);
  }
  .brand__dot {
    position: absolute; left: 54px; top: 252px;
    width: 78px; height: 78px; border-radius: 50%;
    background: var(--wine);
  }
  .brand__name {
    position: absolute; left: 153px; top: 278px;
    font-size: 54px; line-height: 1; font-weight: 600;
    color: var(--wine); white-space: nowrap;
  }
  .brand__sub {
    position: absolute; left: 204px; top: 340px;
    font-size: 22px; line-height: 1; font-weight: 600;
    letter-spacing: 4px; text-transform: uppercase;
    color: var(--wine); white-space: nowrap;
  }
  .social {
    position: absolute; left: 702px; top: 355px;
    display: flex; gap: 13px;
  }
  .social__item { width: 29px; height: 29px; border-radius: 50%; background: var(--wine); }
  .divider {
    position: absolute; left: 54px; top: 390px;
    width: 808px; height: 2px; background: var(--wine);
  }
  .address {
    position: absolute; left: 54px; top: 400px;
    font-size: 20px; line-height: 1.3; color: var(--ink); white-space: nowrap;
  }
  .contact {
    position: absolute; left: 54px; top: 432px;
    display: flex; align-items: center; gap: 7px;
    font-size: 18.5px; line-height: 1.3; color: var(--ink); white-space: nowrap;
  }
  .contact__item { display: flex; align-items: center; gap: 3px; }
  .contact__icon { width: 14px; height: 14px; fill: var(--wine); flex: none; }
</style>
</head>
<body>
  <div class="card">
    <div class="card__watermark" role="img" aria-label="Faint large brand mark decoration"></div>

    <div class="brand__dot"></div>
    <div class="brand__name">Brambleford</div>
    <div class="brand__sub">Wine Cellar</div>

    <div class="social" aria-label="Social profiles">
      <span class="social__item" role="img" aria-label="Social profile one"></span>
      <span class="social__item" role="img" aria-label="Social profile two"></span>
      <span class="social__item" role="img" aria-label="Social profile three"></span>
      <span class="social__item" role="img" aria-label="Social profile four"></span>
    </div>

    <div class="divider"></div>

    <p class="address">42 Ferncastle Steet, Larkwood, Eastmere, Australia 3917</p>

    <div class="contact">
      <span class="contact__item">
        <svg class="contact__icon" viewBox="0 0 16 16" aria-hidden="true"><path d="M3.2 1.5l2.4-.5 1.5 3.4-1.6 1.2c.8 1.8 2.1 3.1 3.9 3.9l1.2-1.6 3.4 1.5-.5 2.4c-.2.8-.9 1.2-1.7 1.1C6.6 12.2 3.8 9.4 2.1 3.2c-.1-.8.3-1.5 1.1-1.7z"/></svg>
        +61 3 9018 4637
      </span>
      <span class="contact__item">
        <svg class="contact__icon" viewBox="0 0 16 16" aria-hidden="true"><path d="M1 3h14v10H1z"/><path d="M1.5 3.8L8 8.8l6.5-5" fill="none" stroke="#eee" stroke-width="1.2"/></svg>
        bramblefordwinecellar@mailvista.com
      </span>
      <span class="contact__item">
        <svg class="contact__icon" viewBox="0 0 16 16" aria-hidden="true"><circle cx="8" cy="8" r="7"/><g fill="none" stroke="#eee" stroke-width="0.9"><ellipse cx="8" cy="8" rx="3" ry="7"/><path d="M1 8h14M2.2 4.5h11.6M2.2 11.5h11.6"/></g></svg>
        www.bramblefordwinecellar.com.au
      </span>
    </div>
  </div>
</body>
</html>
```